Torvane Systems*

Stationary design including business cards, letter heads, envelops and email signatures using our new logo

Target Market(s)

Innovative Technologies

Industry/Entity Type

Defense Contracting

Font styles to use
Sans Serif

```html
<!DOCTYPE html>
<html lang="en">
<head>
<meta charset="utf-8">
<title>Torvane Systems Stationery</title>
<link href="https://fonts.googleapis.com/css2?family=Lato:wght@300;400;700&family=Montserrat:wght@700&family=Oswald:wght@400&display=swap" rel="stylesheet">
<style>
  :root{
    --bg:#d8e3ef;
    --paper:#ffffff;
    --ink:#0a0a0c;
    --text:#555555;
    --muted:#777777;
    --band:#808080;
    --shadow:0 2px 6px rgba(40,60,90,.35);
  }
  *{margin:0;padding:0;box-sizing:border-box}
  html,body{width:1200px;height:831px;overflow:hidden;background:var(--bg)}
  body{position:relative;font-family:"Lato",sans-serif;color:var(--text)}
  .sheet{position:absolute;background:var(--paper);box-shadow:var(--shadow);overflow:hidden}
  .brand{display:flex;align-items:center;gap:5px;font-family:"Oswald",sans-serif;font-weight:400;color:var(--ink);white-space:nowrap;text-transform:uppercase;letter-spacing:-.2px}
  .brand-square{display:block;background:var(--ink)}
  .footer-band{position:absolute;left:0;bottom:0;width:100%}

  /* Letterhead */
  .letterhead{left:117px;top:111px;width:430px;height:609px}
  .letterhead .brand{position:absolute;left:44px;top:84px;font-size:15px}
  .letterhead .brand-square{width:10px;height:10px}
  .contact{position:absolute;left:314px;top:38px;font-size:8px;line-height:9.5px;color:var(--muted)}
  .contact .row{display:flex;align-items:center;gap:7px;height:10.5px}
  .contact .address{margin-bottom:4px}
  .contact svg{width:7px;height:7px}
  .letter{position:absolute;left:41px;top:205px;width:349px}
  .date{font-size:9.5px;font-weight:300;color:var(--muted)}
  .recipient{font-family:"Montserrat",sans-serif;font-weight:700;font-size:14.5px;color:#555;margin-top:4px;letter-spacing:.2px}
  .role{font-size:9.5px;font-weight:300;color:var(--muted);margin-top:3px}
  .body-copy{margin-top:24px;font-size:7.7px;line-height:15px;text-align:justify;color:#555}
  .body-copy p{margin-bottom:15px}
  .closing{font-size:8.7px;margin-top:28px;color:#555}
  .signature{width:46px;height:30px;margin-top:10px;background:linear-gradient(90deg,#e6e6e6,#cfcfcf);border-radius:3px}

  /* Business cards */
  .card-front{left:635px;top:112px;width:183px;height:104px}
  .card-front .brand{position:absolute;right:11px;top:36px;font-size:7px;gap:3px}
  .card-front .brand-square{width:5px;height:5px}
  .card-name{position:absolute;left:11px;top:51px;font-family:"Montserrat",sans-serif;font-weight:700;font-size:8px;color:var(--ink)}
  .card-role{position:absolute;left:11px;top:61px;font-size:4.5px;color:var(--muted)}
  .card-rule{position:absolute;left:11px;top:70px;width:161px;height:.6px;background:#333}
  .card-contact{position:absolute;left:11px;top:75px;font-size:4.4px;line-height:6.8px;color:var(--muted)}
  .card-contact .row{display:flex;align-items:center;gap:4px}
  .card-contact svg{width:4px;height:4px}
  .card-address{position:absolute;right:11px;top:81px;font-size:4.4px;line-height:6.8px;text-align:right;color:var(--muted)}
  .card-back{left:904px;top:111px;width:182px;height:104px;background:var(--ink)}
  .card-back .brand{position:absolute;left:50%;top:50%;transform:translate(-50%,-50%);color:var(--paper);font-size:10px;gap:4px}
  .card-back .brand-square{width:6px;height:6px;background:var(--paper)}

  /* Envelopes */
  .envelope-back{left:635px;top:248px;width:451px;height:226px}
  .flap{position:absolute;left:0;top:0;width:451px;height:66px}
  .envelope-back .brand{position:absolute;left:50%;top:28px;transform:translateX(-50%);color:var(--paper);font-size:9px;gap:4px}
  .envelope-back .brand-square{width:5px;height:5px;background:var(--paper)}
  .envelope-front{left:635px;top:494px;width:451px;height:226px}
  .envelope-front .brand{position:absolute;left:42px;top:88px;font-size:15px}
  .envelope-front .brand-square{width:10px;height:10px}
  .return-address{position:absolute;left:42px;top:182px;font-size:8px;line-height:9.7px;color:var(--muted)}
</style>
</head>
<body>

<svg width="0" height="0" style="position:absolute">
  <defs>
    <symbol id="icon-phone" viewBox="0 0 10 10"><path d="M2 1l2 2-1 1.2c.6 1.2 1.6 2.2 2.8 2.8L7 6l2 2-1.3 1.4C4.5 9.3.7 5.5.6 2.3z" fill="#111"/></symbol>
    <symbol id="icon-mail" viewBox="0 0 10 10"><rect x=".5" y="2" width="9" height="6" fill="#111"/><path d="M.8 2.3L5 5.6l4.2-3.3" stroke="#fff" stroke-width=".8" fill="none"/></symbol>
    <symbol id="icon-web" viewBox="0 0 10 10"><g fill="none" stroke="#111" stroke-width=".9"><circle cx="5" cy="5" r="4.2"/><ellipse cx="5" cy="5" rx="1.8" ry="4.2"/><path d="M.8 5h8.4M1.6 3h6.8M1.6 7h6.8"/></g></symbol>
  </defs>
</svg>

<section class="sheet letterhead" aria-label="Letterhead">
  <div class="brand"><span class="brand-square"></span>Torvane Systems</div>
  <div class="contact">
    <div class="address">1234 First Line Address<br>5678 Second Line Address</div>
    <div class="row"><svg><use href="#icon-phone"/></svg>(777) 888-7777</div>
    <div class="row"><svg><use href="#icon-mail"/></svg>info@yourmail.com</div>
    <div class="row"><svg><use href="#icon-web"/></svg>www.yourwebsite.com</div>
  </div>
  <div class="letter">
    <div class="date">10 December, 2020</div>
    <div class="recipient">DANIEL HARTWELL</div>
    <div class="role">Cheif Executive Officer</div>
    <div class="body-copy">
      <p>Contrary to popular belief, Lorem Ipsum is not simply random text. It has roots in a piece of classical Latin literature from 45 BC, making it over 2000 years old. Arthur Bellweather, a Latin professor at Ashford Ridge College in Virginia, looked up one of the more obscure Latin words, consectetur.</p>
      <p>Lorem Ipsum comes from sections 1.10.32 and 1.10.33 of "de Finibus Bonorum et Malorum" (The Extremes of Good and Evil) by Tullius Maren, written in 45 BC. This book is a treatise on the theory of ethics, very popular during the Renaissance. The first line of Lorem Ipsum.</p>
      <p>The standard chunk of Lorem Ipsum used since the 1500s is reproduced below for those interested.</p>
    </div>
    <div class="closing">Best Regards</div>
    <div class="signature" role="img" aria-label="Handwritten signature"></div>
  </div>
  <svg class="footer-band" width="430" height="20" viewBox="0 0 430 20">
    <rect x="0" y="5" width="326" height="3.5" fill="var(--band)"/>
    <polygon points="336,1 430,1 430,20 0,20 0,15 322,15" fill="var(--ink)"/>
  </svg>
</section>

<section class="sheet card-front" aria-label="Business card front">
  <div class="brand"><span class="brand-square"></span>Torvane Systems</div>
  <div class="card-name">OWEN CALDRY</div>
  <div class="card-role">Founder &amp; CEO</div>
  <div class="card-rule"></div>
  <div class="card-contact">
    <div class="row"><svg><use href="#icon-phone"/></svg>(777) 888-7777</div>
    <div class="row"><svg><use href="#icon-mail"/></svg>info@yourmail.com</div>
    <div class="row"><svg><use href="#icon-web"/></svg>www.yourwebsite.com</div>
  </div>
  <div class="card-address">1234 First Line Address<br>5678 Second Line Address</div>
  <svg class="footer-band" width="183" height="7" viewBox="0 0 183 7">
    <rect x="0" y="1.5" width="138" height="1.3" fill="var(--band)"/>
    <polygon points="143,0 183,0 183,7 0,7 0,4.5 137,4.5" fill="var(--ink)"/>
  </svg>
</section>

<section class="sheet card-back" aria-label="Business card back">
  <div class="brand"><span class="brand-square"></span>Torvane Systems</div>
</section>

<section class="sheet envelope-back" aria-label="Envelope back">
  <svg class="flap" viewBox="0 0 451 66">
    <path d="M0 0H451L447 38Q444 66 416 66H35Q7 66 4 38Z" fill="var(--ink)"/>
  </svg>
  <div class="brand"><span class="brand-square"></span>Torvane Systems</div>
</section>

<section class="sheet envelope-front" aria-label="Envelope front">
  <div class="brand"><span class="brand-square"></span>Torvane Systems</div>
  <div class="return-address">1234 First Line Address<br>5678 Second Line Address</div>
  <svg class="footer-band" width="451" height="18" viewBox="0 0 451 18">
    <rect x="0" y="4" width="342" height="3.5" fill="var(--band)"/>
    <polygon points="353,0 451,0 451,18 0,18 0,13.5 339,13.5" fill="var(--ink)"/>
  </svg>
</section>

</body>
</html>
```